Business Card design for construction company

I would like a business card design for a construction company - Harlow Constructions. I have attached the ai logo file for use. I would like the card to be very smart and clean and incorporate only white and the two colours in the logo. I would like the card to have two sides. One side can just have the logo, the other with the relevant information.

Target Market(s)

Building and Construction Clients

Industry/Entity Type

Business

Contact Information for Business Card

Name: Tom Pardoe
Company: Harlow Constructions Pty Limited
Address: 14 Mallee Crescent Carrow Vale 2093
Phone: 0427 531 068
Email: tomp@harlowbuild-example.com.au

Font styles to use
Serif
Sans Serif

Requirements
Must have
• Details noted above
• Logo as provided
• Colours as in logo
• Square edges
• A font that compliments the logo
Should not have
• Any colour other than white and those in logo
• Rounded edges

```html
<!DOCTYPE html>
<html lang="en">
<head>
<meta charset="utf-8">
<title>Harlow Constructions – Business Card</title>
<link rel="stylesheet" href="https://fonts.googleapis.com/css2?family=Open+Sans:wght@400;600;700&family=Oswald:wght@500&display=swap">
<style>
  :root {
    --backdrop: #ecebe8;
    --card: #ffffff;
    --card-edge: #dcdad6;
    --ink: #4a4b4d;
    --ink-soft: #55565a;
    --accent: #1ea7e8;
  }
  * { margin: 0; padding: 0; box-sizing: border-box; }
  html, body {
    width: 1200px;
    height: 1000px;
    overflow: hidden;
    background: var(--backdrop);
  }
  .canvas {
    position: relative;
    width: 1200px;
    height: 1000px;
  }
  .card {
    position: absolute;
    left: 266px;
    width: 666px;
    height: 397px;
    background: var(--card);
    border: 1px solid var(--card-edge);
    box-shadow: 0 2px 6px rgba(0,0,0,0.08);
  }
  .card--front { top: 74px; }
  .card--back  { top: 533px; }

  .brand-name {
    position: absolute;
    left: 0;
    right: 0;
    top: 180px;
    text-align: center;
    font-family: "Open Sans", sans-serif;
    font-weight: 400;
    font-size: 27px;
    letter-spacing: 3px;
    color: var(--ink);
    text-transform: uppercase;
  }

  .holder-name {
    position: absolute;
    left: 95px;
    top: 176px;
    font-family: "Oswald", sans-serif;
    font-weight: 500;
    font-size: 32px;
    line-height: 1;
    color: var(--ink);
    text-transform: uppercase;
    letter-spacing: -0.3px;
  }
  .divider {
    position: absolute;
    left: 274px;
    top: 179px;
    width: 2px;
    height: 40px;
    background: var(--ink);
  }
  .contact-list {
    position: absolute;
    left: 307px;
    top: 178px;
    list-style: none;
    font-family: "Open Sans", sans-serif;
    font-size: 16px;
    line-height: 21px;
    color: var(--ink);
  }
  .contact-list li {
    display: flex;
    align-items: center;
    gap: 8px;
  }
  .contact-icon { width: 14px; height: 12px; fill: var(--ink); flex: none; }

  .company-line {
    position: absolute;
    left: 0;
    right: 0;
    top: 347px;
    text-align: center;
    font-family: "Open Sans", sans-serif;
    font-size: 16px;
    color: var(--ink-soft);
  }
  .company-line strong { font-weight: 700; }
</style>
</head>
<body>
<main class="canvas">
  <section class="card card--front" aria-label="Card front">
    <p class="brand-name">Harlow Constructions</p>
  </section>

  <section class="card card--back" aria-label="Card back">
    <h1 class="holder-name">Tom Pardoe</h1>
    <span class="divider"></span>
    <ul class="contact-list">
      <li>
        <svg class="contact-icon" viewBox="0 0 14 12" aria-hidden="true">
          <path d="M1 3.2C3.5 0.6 10.5 0.6 13 3.2L11.6 4.8 9.6 3.9V2.9C8 2.3 6 2.3 4.4 2.9V3.9L2.4 4.8Z"/>
          <path d="M3.5 5.2 5 4.6h4l1.5.6L12 11H2Z M7 6.4a1.7 1.7 0 1 0 0 3.4 1.7 1.7 0 1 0 0-3.4Z" fill-rule="evenodd"/>
        </svg>
        <span>0427 531 068</span>
      </li>
      <li>
        <svg class="contact-icon" viewBox="0 0 14 12" aria-hidden="true">
          <path d="M1 2h12v8H1Z M2 3.1v.4l5 3.4 5-3.4v-.4Z" fill-rule="evenodd"/>
        </svg>
        <span>tomp@harlowbuild-example.com.au</span>
      </li>
    </ul>
    <p class="company-line"><strong>Harlow Constructions Pty Limited -</strong> 14 Mallee Crescent Carrow Vale 2093</p>
  </section>
</main>
</body>
</html>
```